Plakat für Schaufenster
Zielgruppe
Moin Moin,
ich habe einen kleinen Fahrradladen in einem historischen Gebäude. Wir führen ein sehr hochwertiges und ausgesuchtes Programm diverser Hersteller und bieten eine umfassende individuelle Beratung
Aufgabenstellung
Ein Fahrradladen ist einerseits ein Handwerksbetrieb anderseits auch ein Handelsbetrieb. Da ich als Einzelkämpfer in meinem Laden arbeite, habe ich diese beiden Betriebe zeitlich voneinander getrennt. Ich arbeite Vormittags in der Werkstatt und Nachmitttags ist mein Laden für Service und Beratung geöffnet, d.h. meine Laden ist nur Nachmittags von 14-18 und Samstag von 10-13 Uhr geöffnet. Durch diese Regelung kann ich kurze Reparaturzeiten und gute Beratung bieten.
Leider denken nun viele Menschen wenn Sie Vormittags vor verschlossener Tür stehen: "der hat es nicht nötig und arbeitet nur noch halbe Tage!".
Nun möchte ich mit einem Plakat im Fenster meinen "geteilten" Betrieb bzw. meine Arbeitsteilung erklären.
Vielleicht in Form einer analogen Uhr mit entsprechender Teilung !?! Aber auch andere Ideen sind herzlich Willkommen !!

```html
<!DOCTYPE html>
<html lang="de">
<head>
<meta charset="utf-8">
<title>Werkstattzeit – Plakatvarianten</title>
<link href="https://fonts.googleapis.com/css2?family=Tinos&display=swap" rel="stylesheet">
<style>
  :root {
    --page-bg: #ffffff;
    --amber-paper: #e8b872;
    --amber-ink: #6b1212;
    --grey-paper: #e9e9e9;
    --grey-ink: #0a0a0a;
    --copper-paper: #e2a663;
    --copper-ink: #ffffff;
    --sage-paper: #bcd5a9;
    --sage-ink: #4d4d4d;
  }
  * { box-sizing: border-box; margin: 0; padding: 0; }
  html, body { width: 1200px; height: 1200px; overflow: hidden; background: var(--page-bg); }
  .sheet-grid { position: relative; width: 1200px; height: 1200px; }

  .poster {
    position: absolute;
    width: 358px;
    height: 477px;
    background: var(--paper);
    color: var(--ink);
    font-family: "Tinos", "Times New Roman", serif;
    text-align: center;
  }
  .poster--amber  { left: 154px; top: 66px;  --paper: var(--amber-paper);  --ink: var(--amber-ink); }
  .poster--grey   { left: 700px; top: 66px;  --paper: var(--grey-paper);   --ink: var(--grey-ink); }
  .poster--copper { left: 154px; top: 667px; --paper: var(--copper-paper); --ink: var(--copper-ink); }
  .poster--sage   { left: 700px; top: 667px; --paper: var(--sage-paper);   --ink: var(--sage-ink); }

  .poster__frame { position: absolute; left: 0; top: 0; width: 358px; height: 477px; }
  .poster__frame path { fill: none; stroke: var(--ink); stroke-width: 1.6; }

  .poster__title, .poster__subtitle, .poster__hours {
    position: absolute; left: 0; width: 100%; line-height: 1; white-space: nowrap;
  }
  .poster__title { top: 58px; font-size: 45px; }
  .poster__subtitle { top: 117px; font-size: 36px; }
  .poster__hours { top: 167px; font-size: 15.5px; line-height: 19.5px; }

  .poster__bike {
    position: absolute; left: 42px; top: 223px; width: 274px; height: 166px;
  }
  .poster__bike rect { fill: var(--ink); opacity: 0.35; }
</style>
</head>
<body>
<main class="sheet-grid">

  <section class="poster poster--amber">
    <svg class="poster__frame" viewBox="0 0 358 477" aria-hidden="true">
      <path d="M32 8 H327 A22 22 0 0 0 349 30 V446 A22 22 0 0 0 327 468 H32 A22 22 0 0 0 10 446 V30 A22 22 0 0 0 32 8 Z"/>
    </svg>
    <h1 class="poster__title">Werkstattzeit</h1>
    <h2 class="poster__subtitle">Service &amp; Beratung</h2>
    <p class="poster__hours">Montag - Freitag 14:00 - 18:00 Uhr<br>Samstag 10:00 &nbsp;- 13:00 Uhr</p>
    <svg class="poster__bike" viewBox="0 0 274 166" role="img" aria-label="Illustration eines historischen Fahrrads, dessen Räder als Uhren die Werkstatt- und Ladenzeiten zeigen">
      <rect width="274" height="166" rx="8"/>
    </svg>
  </section>

  <section class="poster poster--grey">
    <svg class="poster__frame" viewBox="0 0 358 477" aria-hidden="true">
      <path d="M32 8 H327 A22 22 0 0 0 349 30 V446 A22 22 0 0 0 327 468 H32 A22 22 0 0 0 10 446 V30 A22 22 0 0 0 32 8 Z"/>
    </svg>
    <h1 class="poster__title">Werkstattzeit</h1>
    <h2 class="poster__subtitle">Service &amp; Beratung</h2>
    <p class="poster__hours">Montag - Freitag 14:00 - 18:00 Uhr<br>Samstag 10:00 &nbsp;- 13:00 Uhr</p>
    <svg class="poster__bike" viewBox="0 0 274 166" role="img" aria-label="Illustration eines historischen Fahrrads, dessen Räder als Uhren die Werkstatt- und Ladenzeiten zeigen">
      <rect width="274" height="166" rx="8"/>
    </svg>
  </section>

  <section class="poster poster--copper">
    <svg class="poster__frame" viewBox="0 0 358 477" aria-hidden="true">
      <path d="M32 8 H327 A22 22 0 0 0 349 30 V446 A22 22 0 0 0 327 468 H32 A22 22 0 0 0 10 446 V30 A22 22 0 0 0 32 8 Z"/>
    </svg>
    <h1 class="poster__title">Werkstattzeit</h1>
    <h2 class="poster__subtitle">Service &amp; Beratung</h2>
    <p class="poster__hours">Montag - Freitag 14:00 - 18:00 Uhr<br>Samstag 10:00 &nbsp;- 13:00 Uhr</p>
    <svg class="poster__bike" viewBox="0 0 274 166" role="img" aria-label="Illustration eines historischen Fahrrads, dessen Räder als Uhren die Werkstatt- und Ladenzeiten zeigen">
      <rect width="274" height="166" rx="8"/>
    </svg>
  </section>

  <section class="poster poster--sage">
    <svg class="poster__frame" viewBox="0 0 358 477" aria-hidden="true">
      <path d="M32 8 H327 A22 22 0 0 0 349 30 V446 A22 22 0 0 0 327 468 H32 A22 22 0 0 0 10 446 V30 A22 22 0 0 0 32 8 Z"/>
    </svg>
    <h1 class="poster__title">Werkstattzeit</h1>
    <h2 class="poster__subtitle">Service &amp; Beratung</h2>
    <p class="poster__hours">Montag - Freitag 14:00 - 18:00 Uhr<br>Samstag 10:00 &nbsp;- 13:00 Uhr</p>
    <svg class="poster__bike" viewBox="0 0 274 166" role="img" aria-label="Illustration eines historischen Fahrrads, dessen Räder als Uhren die Werkstatt- und Ladenzeiten zeigen">
      <rect width="274" height="166" rx="8"/>
    </svg>
  </section>

</main>
</body>
</html>
```